Social Media Templates for Ambervale Kinship

We need a set of Square (1080 x 1080) social media posts.

My company works with sports clubs, helping them to raise money with a lottery.

I need a set of social media image that I can use to appeal to new Ambervale Kinship to encourage them to start a lottery with us.

This landing page has worked very well for us https://ambervalekinship.com/ambervale-kinship/

THING THAT APPEAL TO CLUBS

No Setup Fees/Start for Free - (We don’t charge any registration fees, or setup fees so you can start raising money from the first draw.)

Start Straight Away - (A club can start raising money straight away.)

Sustainable Income - (The average player plays for 7 years)

Subscription Lottery - (once a player joins, they play until the choose to leave. A club doesn't have to sell tickets every draw to the same people)

All Administration Taken Care Of - (We do all the hard work, so they can focus on running their club.)

Unlimited Income - (There is no limit on the amount of money a club can raise: the more players, the more funds for the club.)

Fundraising reach - (Reach new fans)

50% of the sales is guaranteed profit

£25,000 jackpot - (a person could win £25,000 every week)

Price - (It costs just £1 per week to enter)

Help Your Club - (100% of the profit goes to the club who a player chooses to support)

You can see all the clubs we work with on www.ambervalekinship.com

The images will also be used on Facebook. You can see some examples here https://www.friendvista.com/AmbervaleKinship/ (you may need a proxy to view this page as it is only viewable in the UK, so I have attached some screenshots)

You can find the Ambervale Kinship Logo here https://www.logocrate.com/quillmarshco/

Target Market(s)

People who are involved with amateur sports in United Kingdom

Industry/Entity Type

Gambling

Font styles to use
Sans Serif

Requirements
Must have
• My project must look great on social social media and encourage people to get in touch about starting a lottery with us.

Adobe Suite files must be provided

```html
<!DOCTYPE html>
<html lang="en">
<head>
<meta charset="utf-8">
<title>Saltmere Cove Sailing Club – Lottery Post</title>
<link rel="stylesheet" href="https://fonts.googleapis.com/css2?family=Montserrat:wght@500;600;700;800;900&family=Oswald:wght@500;600&display=swap">
<style>
  :root {
    --navy: #2e3192;
    --white: #ffffff;
    --sky-top: #2fbfee;
    --sky-low: #8fd9ec;
    --sea-top: #1c6cb8;
    --sea-deep: #0b3a7e;
    --band-purple: #34329a;
    --band-cyan: #19f0f5;
    --footer-blue: #3046b2;
    --footer-light: #4a63cc;
  }
  * { margin: 0; padding: 0; box-sizing: border-box; }
  html, body { width: 1173px; height: 1200px; overflow: hidden; background: #1c1c1c; }
  .post {
    position: relative;
    width: 1173px;
    height: 1200px;
    overflow: hidden;
    font-family: "Montserrat", Arial, sans-serif;
  }
  .scene-photo {
    position: absolute; inset: 0;
    background: linear-gradient(180deg, var(--sky-top) 0%, var(--sky-low) 42.5%, var(--sea-top) 43.2%, #135aa4 62%, var(--sea-deep) 100%);
  }
  .headline { position: absolute; left: 0; top: 0; color: var(--navy); line-height: 1; }
  .headline span { position: absolute; white-space: nowrap; }
  .headline .support { left: 49px; top: 80px; font-size: 86px; font-weight: 500; }
  .headline .club-name { left: 52px; top: 165px; font-size: 97px; font-weight: 800; letter-spacing: -1px; }
  .headline .sailing { left: 46px; top: 255px; font-size: 170px; font-weight: 900; letter-spacing: -2px; }
  .headline .club { left: 522px; top: 412px; font-size: 87px; font-weight: 500; }
  .jackpot { position: absolute; color: var(--white); line-height: 1; text-shadow: 3px 5px 8px rgba(0,0,0,.45); font-weight: 700; }
  .jackpot .amount { position: absolute; left: 147px; top: 568px; font-size: 127px; white-space: nowrap; }
  .jackpot .label { position: absolute; left: 116px; top: 683px; font-size: 118px; white-space: nowrap; }
  .brand-mark {
    position: absolute; left: 927px; top: 790px; width: 210px;
    text-align: center; color: var(--white);
    font-family: "Oswald", Arial, sans-serif; font-weight: 500;
    font-size: 34px; line-height: 1.15; text-transform: uppercase;
  }
  .bands { position: absolute; inset: 0; }
  .band-text { position: absolute; white-space: nowrap; line-height: 1; transform-origin: left bottom; }
  .band-text.join { left: 264px; top: 890px; color: var(--white); font-size: 47px; font-weight: 700; transform: rotate(-3.2deg); }
  .band-text.url { left: 212px; top: 985px; color: var(--navy); font-size: 49px; font-weight: 500; transform: rotate(-3.2deg); }
  .price {
    position: absolute; left: 53px; bottom: 30px;
    display: flex; align-items: baseline; gap: 24px;
    color: var(--white); font-weight: 600; line-height: 1;
    text-shadow: 3px 5px 8px rgba(0,0,0,.4);
    white-space: nowrap;
  }
  .price .word { font-size: 116px; }
  .price .amount { font-size: 162px; font-weight: 700; }
</style>
</head>
<body>
<main class="post">
  <div class="scene-photo" role="img" aria-label="Photo of a sailing trimaran with white sails on choppy blue sea under a bright sky, a second yacht behind"></div>

  <h1 class="headline">
    <span class="support">SUPPORT</span>
    <span class="club-name">SALTMERE COVE</span>
    <span class="sailing">SAILING</span>
    <span class="club">CLUB</span>
  </h1>

  <p class="jackpot">
    <span class="amount">£25,000</span>
    <span class="label">JACKPOT</span>
  </p>

  <div class="brand-mark">Ambervale<br>Kinship</div>

  <svg class="bands" width="1173" height="1200" viewBox="0 0 1173 1200" aria-hidden="true">
    <polygon class="band-join" points="262,886 781,858 905,910 232,973" fill="var(--band-purple)"/>
    <polygon class="band-url" points="178,995 976,927 958,988 212,1040" fill="var(--band-cyan)"/>
    <polygon class="footer" points="0,1054 1173,976 1173,1200 0,1200" fill="var(--footer-blue)"/>
    <polygon class="footer-stripe" points="0,1054 480,1022 520,1200 0,1200" fill="var(--footer-light)" opacity=".45"/>
    <polygon class="footer-stripe" points="700,1008 1173,976 1173,1150" fill="#5a74d6" opacity=".3"/>
  </svg>

  <p class="band-text join">JOIN OUR LOTTERY</p>
  <p class="band-text url">www.ambervalekinship.com</p>

  <p class="price">
    <span class="word">JUST</span>
    <span class="amount">£1</span>
    <span class="word">A WEEK</span>
  </p>
</main>
</body>
</html>
```